A private security company called "Tavrin Security Services Ltd"

Hello everybody,

We need a web page for a company based in NZ. It is mainly an informative website so it would be wonderful if the designer puts their absolute best into making it a website that I would really appreciate. The website needs to show professionalism and also needs to make our web surfers find the information they need in a click. the company's colour is black and silver, and if those two colours could be integrated into the website it would be absolutely lovely. Please do contact me for any information.

Sincerely,
Dorian Velasko

Industry/Entity Type

Security

```html
<!DOCTYPE html>
<html lang="en">
<head>
<meta charset="utf-8">
<title>Tavrin Security Services Ltd</title>
<link rel="stylesheet" href="https://fonts.googleapis.com/css2?family=Raleway:wght@400;500;600;700&family=Sorts+Mill+Goudy&family=Open+Sans:wght@400;600&family=Arimo:wght@400&display=swap">
<style>
:root{
  --black:#000;
  --ink:#111;
  --white:#fff;
  --silver-band:#9c9c9c;
  --page-grey:#e3e3e3;
  --panel-grey:#6e6e6e;
  --rule:#c4c4c4;
  --footer:#2f2f2f;
  --footer-text:#b9b9b9;
  --button:#1a1a1a;
}
*{margin:0;padding:0;box-sizing:border-box}
html,body{width:1146px;height:1200px;overflow:hidden;background:var(--white)}
body{position:relative;font-family:"Raleway",sans-serif;color:var(--ink)}
.abs{position:absolute}

/* header */
.social{top:21px;left:899px;display:flex;gap:13px}
.social span{width:32px;height:32px;border-radius:50%;background:#8e8e8e;display:block}
.social span:nth-child(2){background:#a8a8a8}
.social span:nth-child(3){background:#7a7a7a}
.social span:nth-child(4){background:#bdbdbd}
.call{top:68px;left:841px;display:flex;align-items:center;gap:5px;font-family:"Arimo",sans-serif;font-size:19px;color:var(--ink)}
.nav-bar{top:113px;left:0;width:1146px;height:51px;background:var(--black)}
.brand{top:0;left:96px;width:249px;height:164px;background:var(--white);display:flex;flex-direction:column;align-items:center;justify-content:flex-end;padding-bottom:12px;font-family:"Raleway",sans-serif;font-weight:700;color:var(--black)}
.brand .mark{width:44px;height:44px;background:var(--black);margin-bottom:14px}
.brand .name{font-size:34px;letter-spacing:4px;line-height:1}
.brand .sub{font-size:14px;letter-spacing:.5px;margin-top:4px}
.main-nav{top:113px;left:430px;height:51px;display:flex;align-items:center;color:var(--white);font-size:15px;font-weight:500;letter-spacing:.3px}
.main-nav a{color:inherit;text-decoration:none}
.main-nav .sep{margin:0 33px}

/* hero */
.hero{top:165px;left:0;width:1146px;height:382px;background:linear-gradient(100deg,#3a2c22 0%,#6b5038 25%,#8a6a45 45%,#6a5a48 60%,#8c6c46 78%,#4a3a2e 100%)}

/* welcome */
.content-bg{top:609px;left:0;width:1146px;height:503px;background:var(--page-grey)}
.welcome-band{top:563px;left:0;width:1146px;height:46px;background:var(--silver-band)}
.welcome-title{top:570px;left:96px;font-family:"Sorts Mill Goudy",serif;font-size:28px;color:var(--white);letter-spacing:.3px}
.intro{top:625px;left:97px;width:621px;font-size:12.6px;line-height:19.2px;text-align:justify;color:#1c1c1c}
.intro .portrait{float:left;width:121px;height:114px;margin:0 19px 4px 2px;border:2px solid var(--white);background:linear-gradient(160deg,#cfcfcf,#6e6e6e)}
.rule-h{top:814px;left:96px;width:638px;height:1px;background:var(--rule)}
.rule-v{top:838px;left:452px;width:1px;height:242px;background:var(--rule)}
.section-title{font-family:"Sorts Mill Goudy",serif;font-size:27px;color:var(--ink)}

.news-item{left:102px;width:328px}
.news-item .thumb{position:absolute;left:0;top:0;width:56px;height:56px;border:2px solid var(--white);background:linear-gradient(150deg,#bdbdbd,#444)}
.news-item .title{position:absolute;left:70px;top:-2px;font-family:"Arimo",sans-serif;font-size:14px}
.news-item .text{position:absolute;left:70px;top:18px;width:258px;font-family:"Arimo",sans-serif;font-size:12px;line-height:17px;color:#333;text-align:justify}
.news-item .date{position:absolute;right:0;top:56px;font-family:"Arimo",sans-serif;font-style:italic;font-size:12px}
.news-divider{top:968px;left:112px;width:320px;height:1px;background:var(--rule)}
.btn{display:inline-block;background:var(--button);color:var(--white);font-family:"Open Sans",sans-serif;font-size:13px;font-weight:600;padding:3px 5px;border-radius:4px;border:1px solid #888}

.video{top:894px;left:495px;width:232px;height:167px;background:#1b1b1b;border:2px solid #555}
.video .screen{position:absolute;left:4px;top:4px;width:220px;height:140px;background:linear-gradient(135deg,#9a9a9a,#3c3c3c 60%,#777)}
.video .controls{position:absolute;left:4px;bottom:4px;width:220px;height:10px}

/* services panel */
.panel{top:557px;left:800px;width:250px;height:523px}
.panel-title{top:573px;left:807px;font-family:"Sorts Mill Goudy",serif;font-size:23px;color:var(--white)}
.services{top:615px;left:806px;list-style:none}
.services li{position:relative;width:232px;height:26px;margin-bottom:12.3px;padding-left:16px}
.services li span{display:block;background:var(--white);height:26px;line-height:26px;padding-left:7px;font-family:"Open Sans",sans-serif;font-size:14px;color:var(--ink)}
.services li svg{position:absolute;left:1px;top:7px}
.panel-rule{top:851px;left:805px;width:244px;height:1px;background:#9a9a9a}
.testi-title{top:861px;left:816px;font-family:"Sorts Mill Goudy",serif;font-size:24px;color:var(--white)}
.testi-text{top:898px;left:819px;width:207px;font-family:"Raleway",sans-serif;font-size:13px;line-height:19.2px;color:#f0f0f0;text-align:justify}
.testi-text .q{font-family:"Sorts Mill Goudy",serif;font-size:24px;line-height:0;vertical-align:-6px}

/* footer */
.footer{top:1112px;left:0;width:1146px;height:88px;background:var(--footer)}
.footer-nav{top:1136px;left:97px;font-family:"Arimo",sans-serif;font-size:12px;color:var(--footer-text);letter-spacing:.3px}
.footer-nav .sep{margin:0 13px}
.copyright{top:1167px;left:97px;font-family:"Arimo",sans-serif;font-size:11.5px;color:var(--footer-text);letter-spacing:.4px}
.footer-brand{top:1140px;left:950px;width:104px;text-align:center;color:var(--white);font-family:"Raleway",sans-serif;font-weight:700;line-height:1}
.footer-brand .name{font-size:17px;letter-spacing:2px}
.footer-brand .sub{font-size:7px;margin-top:2px}
</style>
</head>
<body>

<header>
  <div class="abs social" aria-label="Social links"><span></span><span></span><span></span><span></span></div>
  <div class="abs call">
    <svg width="18" height="22" viewBox="0 0 18 22" aria-hidden="true"><path d="M4 1c1.5-.6 2.6 0 3 1.4l1 3c.3 1-.2 1.8-1 2.3l-1 .6c.8 2.8 2.2 5.2 4.2 7.2l1-.6c.9-.5 1.8-.4 2.5.4l2 2.3c1 1.1.7 2.4-.5 3.2-1.8 1.2-4 1.3-6-.3C4.8 16.3 2.2 11.7 1.3 6.6.9 4.2 1.9 2 4 1z" fill="#111"/></svg>
    <span>Call us: 555-210-4398</span>
  </div>
  <div class="abs nav-bar"></div>
  <div class="abs brand">
    <span class="mark"></span>
    <span class="name">TAVRIN</span>
    <span class="sub">SECURITY SERVICES LTD.</span>
  </div>
  <nav class="abs main-nav">
    <a href="#">HOME</a><span class="sep">|</span>
    <a href="#">ABOUT</a><span class="sep">|</span>
    <a href="#">SERVICES</a><span class="sep">|</span>
    <a href="#">BLOG</a><span class="sep">|</span>
    <a href="#">CONTACT US</a>
  </nav>
</header>

<div class="abs hero" role="img" aria-label="Photo of uniformed guards in brown uniforms and wide-brimmed hats marching past a crowd"></div>

<main>
  <div class="abs content-bg"></div>
  <div class="abs welcome-band"></div>
  <h1 class="abs welcome-title">Welcome to Tavrin Security Services Ltd.</h1>

  <div class="abs intro">
    <div class="portrait" role="img" aria-label="Black and white photo of a guard in a hat holding a blade"></div>
    Lorem ipsum dolor sit amet, consectetur adipisicing elit, sed do eiusmod tempor incididunt ut labore et dolore magna aliqua. Ut enim ad minim veniam, quis nostrud exercitation ullamco laboris nisi ut aliquip ex ea commodo consequat. Duis aute irure dolor in reprehenderit in voluptate velit esse cillum dolore eu fugiat nulla pariatur. Excepteur sint occaecatLorem ipsum dolor sit amet, consectetur adipisicing elit, sed eiusmod tempor incididuntLorem ipsum dolor consectetur adipisicing elit, sed do eiusmod tempor incididunt ut labore et dolore magna aliqua. Ut enim ad minim veniam, quis nostrud exercitation ullamco laboris nisi ut aliquip ex ea commodo consequat.
  </div>

  <div class="abs rule-h"></div>
  <div class="abs rule-v"></div>

  <h2 class="abs section-title" style="top:838px;left:96px">Update News</h2>
  <article class="abs news-item" style="top:890px">
    <div class="thumb" role="img" aria-label="News thumbnail of a guard"></div>
    <div class="title">Lorem ipsum dolor sit amet,</div>
    <p class="text">consectetur adipisicing elit, sed do eiusmod tempor incididunt ut labore et .</p>
    <div class="date">January 13, 2013</div>
  </article>
  <div class="abs news-divider"></div>
  <article class="abs news-item" style="top:986px">
    <div class="thumb" role="img" aria-label="News thumbnail of a guard"></div>
    <div class="title">Lorem ipsum dolor sit amet,</div>
    <p class="text">consectetur adipisicing elit, sed do eiusmod tempor incididunt ut labore et .</p>
    <div class="date">January 13, 2013</div>
  </article>
  <a class="abs btn" style="top:1074px;left:369px">Read All</a>

  <h2 class="abs section-title" style="top:838px;left:487px">Watch Videos</h2>
  <div class="abs video">
    <div class="screen" role="img" aria-label="Video still of a large group of guards"></div>
    <svg class="abs" style="left:88px;top:45px" width="52" height="52" viewBox="0 0 52 52" aria-hidden="true"><circle cx="26" cy="26" r="24" fill="#fff" fill-opacity=".85"/><circle cx="26" cy="26" r="19" fill="#222"/><path d="M21 16l14 10-14 10z" fill="#fff"/></svg>
    <svg class="controls" viewBox="0 0 220 10" aria-hidden="true"><circle cx="5" cy="5" r="3" fill="#ddd"/><rect x="14" y="4" width="140" height="2" fill="#777"/><rect x="14" y="4" width="8" height="2" fill="#ddd"/><rect x="165" y="3" width="25" height="4" fill="#777"/><rect x="196" y="4" width="16" height="2" fill="#ddd"/></svg>
  </div>
</main>

<aside>
  <svg class="abs panel" viewBox="0 0 250 523" aria-hidden="true"><path d="M0 6L6 0H250V476L125 523L0 476Z" fill="#6e6e6e"/><path d="M0 6L6 0V6Z" fill="#222"/></svg>
  <h3 class="abs panel-title">The services i provide are:</h3>
  <ul class="abs services">
    <li><svg width="12" height="13" viewBox="0 0 12 13"><path d="M2 1l7 5.5L2 12" stroke="#fff" stroke-width="3" fill="none"/></svg><span>Property guards</span></li>
    <li><svg width="12" height="13" viewBox="0 0 12 13"><path d="M2 1l7 5.5L2 12" stroke="#fff" stroke-width="3" fill="none"/></svg><span>Corporate events security</span></li>
    <li><svg width="12" height="13" viewBox="0 0 12 13"><path d="M2 1l7 5.5L2 12" stroke="#fff" stroke-width="3" fill="none"/></svg><span>security consultancy</span></li>
    <li><svg width="12" height="13" viewBox="0 0 12 13"><path d="M2 1l7 5.5L2 12" stroke="#fff" stroke-width="3" fill="none"/></svg><span>private investigation</span></li>
    <li><svg width="12" height="13" viewBox="0 0 12 13"><path d="M2 1l7 5.5L2 12" stroke="#fff" stroke-width="3" fill="none"/></svg><span>personal bodyguard for high</span></li>
    <li><span>net worth individuals</span></li>
  </ul>
  <div class="abs panel-rule"></div>
  <h3 class="abs testi-title">Testimonials</h3>
  <p class="abs testi-text"><span class="q">&ldquo;</span> Lorem ipsum dolor sit amet, consectetur adipisicing elit, sed do eiusmod enim ad minim veniam, quis nostrud exercitation ullamco laboris nisi ut aliquip <span class="q">&rdquo;</span></p>
  <a class="abs btn" style="top:992px;left:968px">Read All</a>
</aside>

<footer>
  <div class="abs footer"></div>
  <nav class="abs footer-nav">HOME<span class="sep">|</span>ABOUT<span class="sep">|</span>SERVICES<span class="sep">|</span>BLOG<span class="sep">|</span>CONTACT US</nav>
  <p class="abs copyright">&copy; 2014 . All right reserved. Privacy Policy | Terms &amp; Conditions</p>
  <div class="abs footer-brand"><div class="name">TAVRIN</div><div class="sub">SECURITY SERVICES LTD.</div></div>
</footer>

</body>
</html>
```